Website Design for new business Brightfield Junior Games

We need a website for our new business Brightfield Junior Games which is about teaching kids from 5 years to 16 years of age how to play either Australian Rules Football or Soccer. Need area for Soccer and Football plus Coaches section, and schedule for each training etc. NEW LOGO ADDED

Target Market(s)

Adults with kids from 5 to 16 looking for specialist coaches to train their kids

Industry/Entity Type

Fitness

Number of Pages Required

5+ page

Colors
3176b5
ffc214

Requirements
Must have
• Logo
• How, Why and What
Nice to have
• I like this website http://www.tallyhoopers.com.au/
• http://www.meadowkickdrills.com.au/ is another site that is okay
Should not have
• Our competitor is this website http://www.pitchcometschooling.com.au/ but I don't like their website style not kid or parent friendly

```html
<!DOCTYPE html>
<html lang="en">
<head>
<meta charset="utf-8">
<title>Brightfield Junior Games</title>
<link rel="stylesheet" href="https://fonts.googleapis.com/css2?family=Oswald:wght@300;400;500&display=swap">
<style>
  :root {
    --navy: #1d2a6b;
    --navy-deep: #16215a;
    --yellow: #ffc214;
    --white: #ffffff;
    --field-bg: #f4f5f7;
    --field-line: #e3e5ea;
    --ink: #2b2f45;
    --muted: #8a8d99;
    --section-bg: #e9ebf1;
    --scrim: rgba(70, 78, 108, 0.42);
  }
  * { box-sizing: border-box; margin: 0; padding: 0; }
  html, body { width: 1200px; height: 960px; overflow: hidden; }
  body {
    position: relative;
    font-family: "Oswald", "Arial Narrow", sans-serif;
    font-weight: 300;
    color: var(--ink);
    background: var(--section-bg);
  }

  /* Hero */
  .hero {
    position: absolute; left: 0; top: 0; width: 1200px; height: 560px;
    background: linear-gradient(180deg, #a9b9cf 0%, #c9d4e2 40%, #e3e8ef 75%, #d5dbe4 100%);
  }
  .hero-kids {
    position: absolute; left: 336px; top: 470px; width: 552px; height: 90px;
    background: linear-gradient(90deg, #6f5a55 0%, #8d3b3c 35%, #5a6c86 65%, #8b3a3f 100%);
  }

  /* Header */
  .brand-ribbon {
    position: absolute; left: 156px; top: 0; width: 127px; height: 110px;
  }
  .brand-name {
    position: absolute; left: 156px; top: 24px; width: 127px;
    text-align: center; color: var(--white);
    font-weight: 500; font-size: 15px; line-height: 18px; text-transform: uppercase;
  }
  .main-nav {
    position: absolute; top: 34px; left: 415px; height: 31px;
    display: flex; align-items: center;
  }
  .main-nav a {
    color: var(--navy); text-decoration: none; font-weight: 400; font-size: 15px;
    margin-right: 29px;
  }
  .nav-cta {
    position: absolute; left: 856px; top: 34px; width: 188px; height: 31px;
    border: 1.5px solid var(--navy); border-radius: 16px;
    display: flex; align-items: center; justify-content: center; gap: 6px;
    color: var(--navy); font-size: 15px; font-weight: 400;
  }

  /* Why section */
  .why-photo {
    position: absolute; left: 156px; top: 588px; width: 444px; height: 372px;
    background: radial-gradient(ellipse at 40% 55%, #2f2f38 0%, #4a4a55 35%, #c9b23a 60%, rgba(233,235,241,0) 80%);
  }
  .why-photo-small {
    position: absolute; left: 804px; top: 912px; width: 84px; height: 48px;
    border-radius: 42px 42px 0 0;
    background: linear-gradient(180deg, #b08a3e, #7a5a2a);
  }
  .why-title {
    position: absolute; left: 612px; top: 632px;
    font-weight: 400; font-size: 31px; color: var(--navy);
  }
  .why-rule {
    position: absolute; left: 588px; top: 682px; width: 100px; height: 1.5px; background: var(--navy);
  }
  .why-text {
    position: absolute; left: 612px; top: 697px; width: 430px; height: 75px; overflow: hidden;
    font-size: 14px; line-height: 18.6px; color: #3b3f55;
  }
  .btn-outline {
    position: absolute; left: 612px; top: 799px; width: 103px; height: 29px;
    border: 1.5px solid var(--navy); border-radius: 15px;
    display: flex; align-items: center; justify-content: center;
    font-size: 13px; font-weight: 400; color: var(--navy);
  }

  .scrim { position: absolute; inset: 0; background: var(--scrim); }

  /* Modal */
  .modal {
    position: absolute; left: 232px; top: 152px; width: 735px; height: 359px;
    background: var(--white); border-top: 12px solid var(--yellow);
    box-shadow: 0 6px 24px rgba(20, 25, 50, 0.18);
  }
  .modal-title {
    position: absolute; left: 76px; top: 45px;
    font-weight: 400; font-size: 31px; color: var(--navy);
  }
  .modal-sub {
    position: absolute; left: 76px; top: 94px; font-size: 15px; color: #44485c;
  }
  .modal-rule { position: absolute; left: 52px; top: 270px; }
  .modal-rule-line {
    position: absolute; left: 52px; top: 118px; width: 100px; height: 1.5px; background: var(--navy);
  }
  .modal-close {
    position: absolute; left: 616px; top: 44px; display: flex; align-items: center; gap: 5px;
    font-size: 15px; color: var(--navy);
  }
  .signup {
    position: absolute; left: 76px; top: 137px; width: 280px; height: 155px;
    background: var(--field-bg); border: 1px solid var(--field-line); border-radius: 3px;
  }
  .field {
    position: absolute; left: 23px; width: 233px; height: 26px;
    background: var(--white); border: 1px solid var(--field-line); border-radius: 3px;
    padding-left: 10px; display: flex; align-items: center;
    font-size: 13px; color: var(--muted);
  }
  .field-name { top: 23px; }
  .field-email { top: 60px; }
  .btn-submit {
    position: absolute; left: 23px; top: 98px; width: 233px; height: 31px;
    background: var(--yellow); border-radius: 3px;
    display: flex; align-items: center; font-size: 14px; font-weight: 400; color: var(--navy-deep);
  }
  .btn-submit-icon {
    width: 38px; height: 100%; display: flex; align-items: center; justify-content: center;
    border-right: 1px solid rgba(0,0,0,0.12); margin-right: 9px;
  }
  .modal-photo {
    position: absolute; left: 381px; top: 137px; width: 279px; height: 154px; border-radius: 3px;
    background: linear-gradient(160deg, #c9d9c2 0%, #9fbf7a 35%, #4f7a3a 70%, #2f4f28 100%);
  }
</style>
</head>
<body>
  <div class="hero" role="img" aria-label="Cloudy sky behind the hero area"></div>
  <div class="hero-kids" role="img" aria-label="Group of kids in team shirts at a sports camp"></div>

  <svg class="brand-ribbon" viewBox="0 0 127 110" aria-hidden="true">
    <polygon points="0,0 127,0 127,110 63.5,92 0,110" fill="#1d2a6b"/>
  </svg>
  <div class="brand-name">Brightfield Junior Games</div>

  <nav class="main-nav">
    <a href="#">Home</a>
    <a href="#">About us</a>
    <a href="#">Our Coaches</a>
    <a href="#">Courses</a>
    <a href="#">News</a>
    <a href="#">Contact Us</a>
  </nav>
  <div class="nav-cta">Where Kids are Champions
    <svg width="9" height="12" viewBox="0 0 9 12" aria-hidden="true"><path d="M4.5 0A4.5 4.5 0 0 0 0 4.5C0 8 4.5 12 4.5 12S9 8 9 4.5A4.5 4.5 0 0 0 4.5 0zm0 6.3a1.8 1.8 0 1 1 0-3.6 1.8 1.8 0 0 1 0 3.6z" fill="#1d2a6b"/></svg>
  </div>

  <section class="why">
    <div class="why-photo" role="img" aria-label="Young football players in helmets, one running with the ball"></div>
    <div class="why-photo-small" role="img" aria-label="Child with curly hair"></div>
    <h2 class="why-title">Why we do it</h2>
    <div class="why-rule"></div>
    <p class="why-text">We are all about getting kids away from computer games and to start living lifein healthy and productive way. We aim to &nbsp;teach the kids how to play their chosen sport, have lots of FUN and help with their personal development for life's challenges. So whether you child wants to become a weekend warrior or just learn the basics, we are here.</p>
    <div class="btn-outline">Know More</div>
  </section>

  <div class="scrim"></div>

  <div class="modal">
    <h2 class="modal-title">Dont Miss Out!</h2>
    <p class="modal-sub">Only Sports Left - Register Your Interest Now</p>
    <div class="modal-rule-line"></div>
    <div class="modal-close">Close
      <svg width="10" height="10" viewBox="0 0 10 10" aria-hidden="true"><path d="M1 1L9 9M9 1L1 9" stroke="#1d2a6b" stroke-width="2.4"/></svg>
    </div>
    <form class="signup">
      <div class="field field-name">Name</div>
      <div class="field field-email">Email</div>
      <div class="btn-submit">
        <span class="btn-submit-icon">
          <svg width="13" height="12" viewBox="0 0 13 12" aria-hidden="true"><path d="M13 0L0 5.5l4 1.6L11 2 5.2 8v4l2.2-2.9L10.5 11z" fill="#16215a"/></svg>
        </span>
        Send me an Information Pack
      </div>
    </form>
    <div class="modal-photo" role="img" aria-label="Young soccer player kicking a ball in a stadium"></div>
  </div>
</body>
</html>
```